Premium Honey Fusions need a label design. 5 awesome blends (see below)

We need a label design for a line of honey. Brand is an existing brand called MELVORIK. www.melvorikusa.example
MELVORIK is a line of juices. The honey line is an extension of the MELVORIK juice line.
Blends are:
Honey Cinnamon
Honey Saffron
Honey Ginger
Honey Herbs
Honey Wild Flower
PRODUCT FROM INDIA
We need a label design for a line of honey. Brand is an existing brand called MELVORIK.
See www.melvorikusa.example
We would like to see label designs that:
-are easy to read, clean
-"Honey Cinnamon”, etc... should be prominent, as it will be what will set us apart.
-use colors that communicate "premium honey"
-premium
-unique
-healthy/good for you
-We need a “Help us save the bees” type message on the logo. We will give % of profit from sale of honey to go towards saving the bees.
The final design should communicate :
-healthy
-DELICIOUS!!!! (it is!)
-premium
-unique
-exotic
Glass bottle is square (see pics) and label has 3 sides:
Front panel
Side panel 1: will be nutritional, ingredients, UPC, etc
Side panel 2: a story about bees? about saffron, about cinnamon??
Target Market(s)
Hispanic and American markets.
Healthy conscious people.
Premium honey market
Look and feel

```html
<!DOCTYPE html>
<html lang="en">
<head>
<meta charset="utf-8">
<title>Melvorik Honey Cinnamon Label</title>
<link href="https://fonts.googleapis.com/css2?family=Comfortaa:wght@400;700&display=swap" rel="stylesheet">
<style>
  :root {
    --page-bg: #f4f4f4;
    --honey-deep: #f0a42a;
    --honey-mid: #f7c45a;
    --honey-pale: #fde7b4;
    --cream: #fffdf7;
    --brand-red: #d8232a;
    --honey-text: #f2a91c;
    --spice-brown: #4a3524;
    --cinnamon: #b5602a;
    --cinnamon-dark: #7e3a14;
    --grey-text: #6f6a64;
    --badge-yellow: #f8c01d;
  }
  * { margin: 0; padding: 0; box-sizing: border-box; }
  html, body { width: 960px; height: 1200px; overflow: hidden; }
  body {
    background: var(--page-bg);
    font-family: "Comfortaa", sans-serif;
    position: relative;
  }
  .label {
    position: absolute;
    left: 80px; top: 125px;
    width: 800px; height: 950px;
    overflow: hidden;
    background: var(--cream);
  }
  .comb-top {
    position: absolute; left: 0; top: 0; width: 100%; height: 520px;
    background: linear-gradient(180deg, var(--honey-deep) 0%, var(--honey-mid) 35%, var(--honey-pale) 70%, rgba(255,253,247,0) 100%);
  }
  .comb-bottom {
    position: absolute; right: 0; bottom: 0; width: 100%; height: 420px;
    background: radial-gradient(ellipse at 85% 90%, var(--honey-mid) 0%, var(--honey-pale) 45%, rgba(255,253,247,0) 75%);
  }
  .center-glow {
    position: absolute; left: 60px; top: 380px; width: 680px; height: 260px;
    background: radial-gradient(ellipse at center, var(--cream) 40%, rgba(255,253,247,0) 75%);
  }
  .brand-name {
    position: absolute; left: 0; right: 0; top: 160px;
    text-align: center;
    font-weight: 700; font-size: 96px; letter-spacing: 2px;
    color: var(--brand-red);
  }
  .flavour {
    position: absolute; left: 0; right: 0; top: 430px;
    text-align: center;
  }
  .flavour-base {
    display: block;
    font-weight: 700; font-size: 92px; line-height: 1;
    color: var(--honey-text);
    padding-left: 150px;
  }
  .flavour-name {
    display: block;
    font-weight: 700; font-size: 60px; line-height: 1; letter-spacing: 2px;
    color: var(--spice-brown);
    margin-top: 18px;
    padding-left: 150px;
  }
  .spice-photo {
    position: absolute; left: 30px; top: 640px; width: 420px; height: 160px;
    background: linear-gradient(160deg, var(--cinnamon) 0%, var(--cinnamon-dark) 100%);
    border-radius: 40px;
    opacity: 0.9;
  }
  .bee-badge {
    position: absolute; left: 448px; top: 690px; width: 180px; height: 180px;
  }
  .net-weight {
    position: absolute; left: 0; width: 720px; top: 860px;
    text-align: center;
    font-size: 30px; color: var(--grey-text);
  }
</style>
</head>
<body>
  <main class="label">
    <div class="comb-top" role="img" aria-label="Honeycomb pattern in warm amber tones"></div>
    <div class="comb-bottom" role="img" aria-label="Honeycomb pattern fading into the corner"></div>
    <div class="center-glow"></div>

    <div class="brand-name">MELVORIK</div>

    <h1 class="flavour">
      <span class="flavour-base">honey</span>
      <span class="flavour-name">CINNAMON</span>
    </h1>

    <div class="spice-photo" role="img" aria-label="Photograph of cinnamon sticks"></div>

    <svg class="bee-badge" viewBox="0 0 180 180" aria-label="Help us save the bees badge">
      <defs>
        <path id="badge-arc" d="M 30 112 A 64 64 0 1 1 150 112"/>
      </defs>
      <circle cx="90" cy="90" r="86" fill="#ffffff"/>
      <circle cx="90" cy="90" r="80" fill="var(--badge-yellow)"/>
      <text font-family="Comfortaa, sans-serif" font-size="15" font-weight="700" fill="var(--spice-brown)" letter-spacing="1">
        <textPath href="#badge-arc" startOffset="50%" text-anchor="middle">HELP US SAVE THE BEES</textPath>
      </text>
      <circle cx="90" cy="108" r="32" fill="#e8a515" role="img" aria-label="Cartoon bee illustration"/>
    </svg>

    <div class="net-weight">500gm</div>
  </main>
</body>
</html>
```